Improving a camping website homepage header*

My client is very happy with his new website and its new functionalities. However, he's not very happy about the homepage design. Specifically, the header(this includes the menu, large header image and two columns beneath that). You can find the website here: http://lnkvo.example/siteTentra .

He forwarded me several other websites he likes. Which can be found in the attachments. I also included several pictures of the camping.

I'm looking for a design that will improve the header of the homepage with room for other global style chances. The logo cannot be changed.

Attachments
1) His old website homepage
2) Website mockup he liked.
3) Another website mockup he liked.

Other images can be found on the new website http://lnkvo.example/siteTentra or his old website http://lnkvo.example/formerSiteTentra.

Can you help us?
Updates

Hello guys. Here's a bit more information - Language used on the website is dutch. - The two columns left/right are supposed to link to Hire/Buy chalets. The client indicated that he finds these links important, but doesn't like the current design. I think this is partially the case because he doesn't like the icons. I'm looking forward to your designs!

Target Market(s)

30-50 year old wealthy people that want to purchase or rent cabins in the Netherlands.

Number of Pages Required

1 page

Colors

Designer to choose colors to be used in the design.

Requirements
Must have
• Improved header
Nice to have
• Global style changes
Should not have
• Logo changes

```html
<!DOCTYPE html>
<html lang="nl">
<head>
<meta charset="utf-8">
<title>Parc Lindehof – Home</title>
<link rel="stylesheet" href="https://fonts.googleapis.com/css2?family=Open+Sans:wght@400;600;700&display=swap">
<style>
  :root {
    --green: #7a9a1e;
    --orange: #df7a10;
    --ink: #555555;
    --white: #ffffff;
    --line: #6a6a6a;
    --photo-dark: #2a2a24;
    --photo-mid: #5d5747;
    --photo-teal: #4f7f86;
  }
  * { box-sizing: border-box; margin: 0; padding: 0; }
  html, body { width: 1200px; height: 750px; overflow: hidden; background: var(--white); }
  body { position: relative; font-family: "Open Sans", sans-serif; }

  .top-strip {
    position: absolute; left: 0; top: 0; width: 1200px; height: 42px;
    background: linear-gradient(90deg, #6d6452 0%, #8c8470 35%, #5e5a4c 65%, #7f7564 100%);
  }

  .site-header {
    position: absolute; left: 0; top: 42px; width: 1200px; height: 66px;
    background: var(--white);
  }
  .brand {
    position: absolute; left: 58px; top: 19px;
    display: flex; align-items: center; gap: 8px;
    color: var(--green); font-size: 18px; font-weight: 600; text-decoration: none;
  }
  .brand-dot { width: 22px; height: 22px; border-radius: 50%; background: var(--green); }

  .main-nav {
    position: absolute; left: 352px; top: 0; height: 66px;
    display: flex; align-items: center; gap: 23px;
  }
  .main-nav a {
    position: relative; font-size: 13px; color: var(--ink); text-decoration: none;
  }
  .main-nav a.is-active { color: var(--green); font-weight: 600; }
  .main-nav a.is-active::after {
    content: ""; position: absolute; left: 0; right: 0; bottom: -6px;
    height: 2px; background: var(--green);
  }
  .login-button {
    position: absolute; left: 1057px; top: 19px; width: 82px; height: 28px;
    border: 1.5px solid var(--line); border-radius: 14px;
    display: flex; align-items: center; justify-content: center;
    font-size: 12px; color: var(--ink); text-decoration: none;
  }

  .hero {
    position: absolute; left: 0; top: 108px; width: 1200px; height: 529px;
    overflow: hidden;
  }
  .hero-photo {
    position: absolute; inset: 0;
    background:
      radial-gradient(ellipse at 70% 30%, rgba(79,127,134,0.55) 0%, rgba(79,127,134,0) 45%),
      linear-gradient(180deg, #6b6452 0%, var(--photo-mid) 40%, #3b382e 75%, #1c1b17 100%);
  }
  .hero-shade {
    position: absolute; inset: 0;
    background: linear-gradient(90deg, rgba(0,0,0,0.35) 0%, rgba(0,0,0,0.1) 60%, rgba(0,0,0,0) 100%);
  }
  .slider-arrows { position: absolute; left: 147px; top: 167px; }
  .hero-title {
    position: absolute; left: 143px; top: 290px; transform: translateY(-100%);
    top: 252px;
    font-size: 83px; font-weight: 600; line-height: 1; color: var(--white);
    letter-spacing: -0.5px;
  }
  .hero-title { transform: none; top: 187px; }
  .hero-text {
    position: absolute; left: 148px; top: 282px; width: 460px;
    font-size: 17px; line-height: 25px; color: var(--white);
  }
  .contact-button {
    position: absolute; left: 149px; top: 391px; width: 167px; height: 42px;
    border-radius: 21px; background: var(--orange);
    display: flex; align-items: center; justify-content: center;
    font-size: 14px; font-weight: 600; color: var(--white); text-decoration: none;
  }
  .phone-icon { position: absolute; left: 366px; top: 383px; }
  .phone-number {
    position: absolute; left: 442px; top: 400px;
    font-size: 17px; font-weight: 600; color: var(--white); line-height: 24px;
  }
</style>
</head>
<body>
  <div class="top-strip" role="img" aria-label="Luchtfoto van daken van vakantiehuizen"></div>

  <header class="site-header">
    <a class="brand" href="#"><span class="brand-dot"></span>Parc Lindehof</a>
    <nav class="main-nav">
      <a href="#" class="is-active">Home</a>
      <a href="#">Het Park</a>
      <a href="#">Financiering</a>
      <a href="#">Chalets</a>
      <a href="#">Aanbiedingen</a>
      <a href="#">Faciliteiten</a>
      <a href="#">Contact</a>
    </nav>
    <a class="login-button" href="#">Inloggen</a>
  </header>

  <section class="hero">
    <div class="hero-photo" role="img" aria-label="Luchtfoto van een park met chalets tussen de bomen"></div>
    <div class="hero-shade"></div>

    <svg class="slider-arrows" width="42" height="20" viewBox="0 0 42 20" aria-hidden="true">
      <polyline points="9,3 3,10 9,17" fill="none" stroke="#cfcfcf" stroke-width="1.5"/>
      <polyline points="33,3 39,10 33,17" fill="none" stroke="#df7a10" stroke-width="1.5"/>
    </svg>

    <h1 class="hero-title">Rent a chalet</h1>
    <p class="hero-text">Lorem ipsum dolor sit amet, consectetur adipiscing elit. Aenean euismod bibendum laoreet. Proin gravida dolor sit amet lacus accumsan and viverra justo commodo.</p>

    <a class="contact-button" href="#">Contact Us</a>

    <svg class="phone-icon" width="58" height="58" viewBox="0 0 58 58" aria-hidden="true">
      <circle cx="29" cy="29" r="28" fill="none" stroke="rgba(255,255,255,0.45)" stroke-width="1"/>
      <circle cx="29" cy="29" r="25" fill="none" stroke="#ffffff" stroke-width="1.5"/>
      <circle cx="29" cy="29" r="21" fill="#ffffff"/>
      <path d="M22.5 21.5 l3.5 -1.2 l2.4 5 l-2.2 1.6 c1 2.4 2.6 4 5 5 l1.6 -2.2 l5 2.4 l-1.2 3.5 c-7.4 0.2 -14.3 -6.7 -14.1 -14.1 z" fill="#333333"/>
    </svg>
    <span class="phone-number">0300 - 48 27 19</span>
  </section>
</body>
</html>
```